RK Bastone Construction Inc.

Design a new business card for our construction company
To be removed from current card:
Delete 25 years
Delete Tenant fit up Renovations section

```html
<!DOCTYPE html>
<html lang="en">
<head>
<meta charset="utf-8">
<title>RK Bastone Construction Inc. – Business Card</title>
<link rel="stylesheet" href="https://fonts.googleapis.com/css2?family=Montserrat:wght@400;500;600;700&display=swap">
<style>
  :root {
    --teal: #237a6f;
    --teal-dark: #1f7067;
    --purple: #5b2a7e;
    --ink: #3a3a3a;
    --paper: #ffffff;
    --backdrop: #3b3b3b;
  }
  * { box-sizing: border-box; margin: 0; padding: 0; }
  html, body { width: 1200px; height: 1200px; overflow: hidden; }
  body {
    background: var(--backdrop);
    font-family: "Montserrat", sans-serif;
    position: relative;
  }
  .card {
    position: absolute;
    left: 180px;
    width: 840px;
    height: 480px;
    border-radius: 34px;
    overflow: hidden;
  }
  .card--front { top: 90px; background: var(--paper); }
  .card--back { top: 630px; background: var(--teal); }

  .name-band {
    position: absolute;
    left: 0; top: 200px;
    width: 400px; height: 170px;
    background: var(--teal);
    color: var(--paper);
    padding: 30px 0 0 44px;
  }
  .person-name {
    font-size: 27px; font-weight: 600; letter-spacing: 0.5px;
    margin-bottom: 14px;
  }
  .person-line {
    display: flex; align-items: center; gap: 12px;
    font-size: 16px; font-weight: 400; margin-bottom: 8px;
  }
  .person-line svg { width: 18px; height: 18px; flex: none; }
  .accent-bar {
    position: absolute;
    left: 420px; top: 165px;
    width: 16px; height: 205px;
    background: var(--purple);
  }
  .company-name {
    position: absolute;
    left: 470px; top: 70px;
    color: var(--teal);
    font-weight: 700;
    font-size: 29px;
    line-height: 1.1;
    letter-spacing: 0.5px;
    text-transform: uppercase;
  }
  .company-contact {
    position: absolute;
    left: 470px; top: 175px;
    color: var(--ink);
    font-size: 15.5px;
    line-height: 1.35;
  }
  .company-contact li {
    list-style: none;
    display: flex; align-items: flex-start; gap: 10px;
    margin-bottom: 3px;
  }
  .company-contact svg { width: 17px; height: 17px; flex: none; margin-top: 2px; }
  .services {
    position: absolute;
    left: 340px; top: 392px;
    width: 460px;
    text-align: center;
    font-weight: 600;
    letter-spacing: 0.6px;
    text-transform: uppercase;
  }
  .services-main { color: var(--ink); font-size: 15.5px; }
  .services-sectors { color: var(--teal); font-size: 14.5px; margin-top: 4px; }

  .back-name {
    position: absolute;
    left: 100px; top: 160px;
    color: var(--paper);
    font-weight: 700;
    font-size: 60px;
    line-height: 1.05;
    letter-spacing: 1px;
    text-transform: uppercase;
  }
</style>
</head>
<body>
  <section class="card card--front" aria-label="Business card front">
    <div class="name-band">
      <p class="person-name">DARIO BASTONE</p>
      <p class="person-line">
        <svg viewBox="0 0 24 24" fill="none" stroke="currentColor" stroke-width="2"><rect x="6" y="2" width="12" height="20" rx="2"/><line x1="11" y1="18" x2="13" y2="18"/></svg>
        613-555-0148
      </p>
      <p class="person-line">
        <svg viewBox="0 0 24 24" fill="none" stroke="currentColor" stroke-width="2"><rect x="2" y="5" width="20" height="14"/><polyline points="2,5 12,13 22,5"/></svg>
        dario@rkbastoneconst.ca
      </p>
    </div>
    <div class="accent-bar"></div>

    <p class="company-name">RK Bastone<br>Construction Inc.</p>

    <ul class="company-contact">
      <li>
        <svg viewBox="0 0 24 24" fill="var(--teal)"><path d="M6.6 10.8a15 15 0 0 0 6.6 6.6l2.2-2.2a1 1 0 0 1 1-.25 11.4 11.4 0 0 0 3.6.57 1 1 0 0 1 1 1V20a1 1 0 0 1-1 1A17 17 0 0 1 3 4a1 1 0 0 1 1-1h3.5a1 1 0 0 1 1 1c0 1.25.2 2.45.57 3.57a1 1 0 0 1-.25 1z"/></svg>
        613-555-0192 ext. 221
      </li>
      <li>
        <svg viewBox="0 0 24 24" fill="none" stroke="var(--teal)" stroke-width="2"><circle cx="12" cy="12" r="10"/><line x1="2" y1="12" x2="22" y2="12"/><ellipse cx="12" cy="12" rx="4.5" ry="10"/></svg>
        www.rkbastoneconstruction.ca
      </li>
      <li>
        <svg viewBox="0 0 24 24" fill="none" stroke="var(--teal)" stroke-width="2.2"><path d="M12 22s7-6.5 7-12a7 7 0 0 0-14 0c0 5.5 7 12 7 12z"/><circle cx="12" cy="10" r="2.5"/></svg>
        <span>2175 Meridian Rd.<br>Suite 100, Ottawa, ON K1B 4N7</span>
      </li>
    </ul>

    <div class="services">
      <p class="services-main">Turn Key Operations | Project Management</p>
      <p class="services-sectors">Office | Retail | Institutional</p>
    </div>
  </section>

  <section class="card card--back" aria-label="Business card back">
    <p class="back-name">RK Bastone<br>Construction Inc.</p>
  </section>
</body>
</html>
```